Business Card Design

I need a business card for a new company based in Australia called "ClinoPath".

Its a cloud program for GPs that allows them to search for the specialist they require using a simple user friendly tool.

I would like the colours to match those in the program (the colours in the logo attached).

The final design should reflect the programs clarity, ease of use and professionalism.

Target Market(s)

GPs and other Health Professionals

Industry/Entity Type

Business

Contact Information for Business Card

ClinoPath; The Whole Consultant Index; Maren Tolhurst CEO; 0417385261; maren@clinopath.example; www.clinopath.example

Requirements
Must have
• Must have the logo attached; the web address and my name and phone number
Nice to have
• the slogan "The Whole Consultant Index"

```html
<!DOCTYPE html>
<html lang="en">
<head>
<meta charset="utf-8">
<title>ClinoPath Business Card</title>
<link rel="stylesheet" href="https://fonts.googleapis.com/css2?family=Didact+Gothic&family=Open+Sans:wght@400;700&display=swap">
<style>
  :root {
    --page-bg: #eceff2;
    --card-white: #ffffff;
    --brand-blue: #1aa3dc;
    --blue-light: #1fcaf0;
    --blue-mid: #0a9bd8;
    --blue-deep: #0066b8;
    --swoosh-grey: #a9adb2;
    --text-grey: #8a8f95;
    --text-dark: #1f2326;
  }
  * { margin: 0; padding: 0; box-sizing: border-box; }
  html, body { width: 1200px; height: 913px; overflow: hidden; }
  body {
    background: var(--page-bg);
    position: relative;
    font-family: "Open Sans", Arial, sans-serif;
  }
  .card {
    position: absolute;
    width: 520px;
    height: 297px;
    background: var(--card-white);
    overflow: hidden;
    box-shadow: 0 6px 22px rgba(0,0,0,0.14);
  }
  .card-front { left: 60px; top: 308px; }
  .card-back  { left: 620px; top: 308px; }
  .card-art { position: absolute; inset: 0; width: 100%; height: 100%; }

  .wordmark {
    position: absolute;
    font-family: "Didact Gothic", "Century Gothic", sans-serif;
    color: var(--brand-blue);
    line-height: 1;
  }
  .wordmark-name { display: flex; align-items: center; gap: 8px; letter-spacing: -0.5px; }
  .wordmark-dot { width: 8px; height: 8px; border-radius: 50%; background: var(--brand-blue); }
  .wordmark-tagline {
    font-family: "Didact Gothic", "Century Gothic", sans-serif;
    color: var(--text-grey);
    margin-top: 3px;
    letter-spacing: 0.2px;
  }
  .card-front .wordmark { left: 34px; top: 122px; }
  .card-front .wordmark-name { font-size: 40px; }
  .card-front .wordmark-tagline { font-size: 12.5px; }
  .card-back .wordmark { left: 215px; top: 120px; }
  .card-back .wordmark-name { font-size: 46px; }
  .card-back .wordmark-tagline { font-size: 14px; }

  .person {
    position: absolute;
    right: 128px;
    top: 112px;
    text-align: right;
  }
  .person-name { font-size: 15px; font-weight: 700; color: var(--brand-blue); }
  .person-role { font-size: 12px; color: var(--text-dark); margin-top: 1px; }

  .contact-list {
    position: absolute;
    left: 34px;
    bottom: 28px;
    list-style: none;
  }
  .contact-item {
    display: flex;
    align-items: center;
    gap: 8px;
    font-size: 12.5px;
    color: var(--text-dark);
    line-height: 19px;
  }
  .contact-icon { width: 11px; height: 11px; flex: none; }
</style>
</head>
<body>

<section class="card card-front" aria-label="Business card front">
  <svg class="card-art" viewBox="0 0 520 297" aria-hidden="true">
    <defs>
      <linearGradient id="front-blue" x1="0" y1="0" x2="0.4" y2="1">
        <stop offset="0" stop-color="var(--blue-light)"/>
        <stop offset="1" stop-color="var(--blue-mid)"/>
      </linearGradient>
    </defs>
    <path d="M150 0 L520 0 L520 297 L478 297 C470 150 380 20 150 0 Z" fill="url(#front-blue)"/>
    <path d="M150 0 C380 20 470 150 478 297" fill="none" stroke="var(--swoosh-grey)" stroke-width="5"/>
    <path d="M150 0 C370 26 458 150 466 297" fill="none" stroke="#ffffff" stroke-width="6"/>
  </svg>

  <div class="wordmark">
    <div class="wordmark-name">ClinoPath<span class="wordmark-dot"></span></div>
    <div class="wordmark-tagline">The Whole Consultant Index</div>
  </div>

  <div class="person">
    <div class="person-name">Maren Tolhurst</div>
    <div class="person-role">CEO</div>
  </div>

  <ul class="contact-list">
    <li class="contact-item">
      <svg class="contact-icon" viewBox="0 0 12 12" aria-hidden="true"><rect x="3" y="0.5" width="6" height="11" rx="1.2" fill="none" stroke="var(--brand-blue)" stroke-width="1.3"/></svg>
      0417385261
    </li>
    <li class="contact-item">
      <svg class="contact-icon" viewBox="0 0 12 12" aria-hidden="true"><rect x="0.7" y="2" width="10.6" height="8" fill="none" stroke="var(--brand-blue)" stroke-width="1.3"/><path d="M0.7 2 L6 7 L11.3 2" fill="none" stroke="var(--brand-blue)" stroke-width="1.3"/></svg>
      maren@clinopath.example
    </li>
    <li class="contact-item">
      <svg class="contact-icon" viewBox="0 0 12 12" aria-hidden="true"><circle cx="6" cy="6" r="5.3" fill="none" stroke="var(--brand-blue)" stroke-width="1.2"/><ellipse cx="6" cy="6" rx="2.3" ry="5.3" fill="none" stroke="var(--brand-blue)" stroke-width="1"/><path d="M0.7 6 H11.3" stroke="var(--brand-blue)" stroke-width="1"/></svg>
      www.clinopath.example
    </li>
  </ul>
</section>

<section class="card card-back" aria-label="Business card back">
  <svg class="card-art" viewBox="0 0 520 297" aria-hidden="true">
    <defs>
      <linearGradient id="back-blue" x1="0" y1="0" x2="0.3" y2="1">
        <stop offset="0" stop-color="var(--blue-light)"/>
        <stop offset="1" stop-color="var(--blue-deep)"/>
      </linearGradient>
    </defs>
    <path d="M0 0 L318 0 C200 40 110 150 92 297 L0 297 Z" fill="url(#back-blue)"/>
    <path d="M318 0 C200 40 110 150 92 297" fill="none" stroke="var(--swoosh-grey)" stroke-width="5"/>
    <path d="M330 0 C214 42 124 150 106 297" fill="none" stroke="#ffffff" stroke-width="8"/>
  </svg>

  <div class="wordmark">
    <div class="wordmark-name">ClinoPath<span class="wordmark-dot"></span></div>
    <div class="wordmark-tagline">The Whole Consultant Index</div>
  </div>
</section>

</body>
</html>
```